Business Card For Kelmora Financial Consulting

Hi, I would like a business card designed. Bold, modern.
Please use the same design as the logo. I have also attached the website design to see the overall theme.
Wordmark Font
Color: Hex: #01AEF7

```html
<!DOCTYPE html>
<html lang="en">
<head>
<meta charset="utf-8">
<title>Kelmora Financial Consulting – Business Card</title>
<link rel="stylesheet" href="https://fonts.googleapis.com/css2?family=Jost:wght@400;500;600&display=swap">
<style>
  :root {
    --page: #e9ecef;
    --ink-dark: #131d26;
    --ink-deep: #070d15;
    --brand-blue: #01aef7;
    --panel-blue: #3aa8e0;
    --panel-blue-light: #4db6ea;
    --edge-blue: #1a6f9e;
    --text-light: #e8edf1;
    --text-on-blue: #12364f;
  }
  * { box-sizing: border-box; margin: 0; padding: 0; }
  html, body {
    width: 1200px; height: 900px; overflow: hidden;
    background: var(--page);
    font-family: "Jost", sans-serif;
  }
  .canvas { position: relative; width: 1200px; height: 900px; }
  .card {
    position: absolute; left: 320px; width: 560px; height: 320px;
    overflow: hidden; border-radius: 3px;
    box-shadow: 0 10px 28px rgba(0,0,0,.22);
  }
  .card--back { top: 70px; }
  .card--front { top: 470px; background: var(--ink-dark); }

  .back-pattern {
    position: absolute; inset: 0;
    background: radial-gradient(ellipse at 45% 45%, #15222e 0%, #0c1620 55%, var(--ink-deep) 100%);
  }
  .back-name {
    position: absolute; right: 40px; bottom: 92px;
    display: flex; align-items: center; gap: 10px;
    color: var(--brand-blue); font-weight: 500; font-size: 15px;
    letter-spacing: .12em; text-transform: uppercase;
  }
  .mark-square {
    width: 22px; height: 22px; border: 3px solid var(--brand-blue);
  }

  .front-shapes { position: absolute; inset: 0; }

  .wordmark {
    position: absolute; left: 34px; top: 34px;
    display: flex; align-items: center; gap: 14px;
  }
  .wordmark .mark-square { width: 44px; height: 44px; border-width: 4px; }
  .wordmark-text {
    color: var(--text-light); font-weight: 600; font-size: 22px;
    line-height: 1.1; letter-spacing: .06em; text-transform: uppercase;
  }

  .person { position: absolute; left: 80px; top: 188px; }
  .person-name {
    color: var(--brand-blue); font-weight: 600; font-size: 19px;
    letter-spacing: .03em; text-transform: uppercase;
  }
  .person-role { color: var(--text-light); font-size: 13px; margin-top: -2px; margin-left: 8px; }

  .contacts {
    position: absolute; left: 88px; top: 240px; list-style: none;
    color: var(--text-light); font-size: 12.5px; line-height: 21px;
  }
  .contacts li { display: flex; align-items: center; gap: 8px; }
  .contacts svg { width: 12px; height: 12px; fill: var(--brand-blue); flex: none; }

  .address {
    position: absolute; right: 30px; bottom: 84px; text-align: right;
    color: var(--text-on-blue); font-size: 13px; line-height: 18px;
  }
</style>
</head>
<body>
<main class="canvas">

  <section class="card card--back" aria-label="Card back">
    <div class="back-pattern" role="img" aria-label="Dark navy background with a faint repeating brand-mark pattern"></div>
    <div class="back-name">
      <span class="mark-square"></span>
      <span>Kelmora Financial Consulting</span>
    </div>
  </section>

  <section class="card card--front" aria-label="Card front">
    <svg class="front-shapes" viewBox="0 0 560 320" width="560" height="320" aria-hidden="true">
      <defs>
        <linearGradient id="blue-panel" x1="0" y1="0" x2="1" y2="1">
          <stop offset="0" stop-color="#2f9fd9"/>
          <stop offset="1" stop-color="#4db6ea"/>
        </linearGradient>
      </defs>
      <polygon points="236,0 406,0 296,320 276,320" fill="#ffffff" opacity="0.09"/>
      <polygon points="404,0 560,0 560,320 282,320" fill="var(--edge-blue)"/>
      <polygon points="414,0 560,0 560,320 294,320" fill="url(#blue-panel)"/>
      <polygon points="470,0 560,0 560,120" fill="#ffffff" opacity="0.08"/>
    </svg>

    <div class="wordmark">
      <span class="mark-square"></span>
      <span class="wordmark-text">Kelmora<br>Financial Consulting</span>
    </div>

    <div class="person">
      <p class="person-name">Alex Morgan</p>
      <p class="person-role">Manager</p>
    </div>

    <ul class="contacts">
      <li>
        <svg viewBox="0 0 24 24"><path d="M6.6 10.8a15.1 15.1 0 0 0 6.6 6.6l2.2-2.2a1 1 0 0 1 1-.25 11.4 11.4 0 0 0 3.6.57 1 1 0 0 1 1 1V20a1 1 0 0 1-1 1A17 17 0 0 1 3 4a1 1 0 0 1 1-1h3.5a1 1 0 0 1 1 1c0 1.25.2 2.45.57 3.57a1 1 0 0 1-.25 1z"/></svg>
        (041) 582 30417
      </li>
      <li>
        <svg viewBox="0 0 24 24"><path d="M2 5h20v14H2zm2 2v.5l8 5 8-5V7zm0 2.9V17h16V9.9l-8 5z"/></svg>
        info@kelmoraconsulting.com
      </li>
      <li>
        <svg viewBox="0 0 24 24"><path d="M12 2a10 10 0 1 0 0 20 10 10 0 0 0 0-20zm6.9 6h-3a15 15 0 0 0-1.3-3.9A8 8 0 0 1 18.9 8zM12 4c.9 1.2 1.6 2.6 2 4h-4c.4-1.4 1.1-2.8 2-4zM4.3 14a8 8 0 0 1 0-4h3.4a16 16 0 0 0 0 4zm.8 2h3a15 15 0 0 0 1.3 3.9A8 8 0 0 1 5.1 16zm3-8h-3a8 8 0 0 1 4.3-3.9A15 15 0 0 0 8.1 8zM12 20c-.9-1.2-1.6-2.6-2-4h4c-.4 1.4-1.1 2.8-2 4zm2.3-6H9.7a14 14 0 0 1 0-4h4.6a14 14 0 0 1 0 4zm.3 5.9a15 15 0 0 0 1.3-3.9h3a8 8 0 0 1-4.3 3.9zm1.7-5.9a16 16 0 0 0 0-4h3.4a8 8 0 0 1 0 4z"/></svg>
        www.kelmoraconsulting.com
      </li>
    </ul>

    <address class="address">
      2718 Larkspur Avenue<br>
      Brookhaven, FL 32804
    </address>
  </section>

</main>
</body>
</html>
```